Rebrand of 3 bottle labels for nail polish brand

The task is to make a rebranding of our current gel nail polish bottle design. We have become one of the leading european nail polish brand, so we want to improve the quality of the label design to a more scandinavian and minimalistic bottle design, which stille has to be recognisable and unique.

We have attached a more detailed description of the rebranding instructions for our gel polish bottles called "bottle task".
Updates

The Labels should not be just Black and White as stated. But should be mainly Black and White and then some of our color as explained in the uploaded file.

Target Market(s)

Girls and women age 18-55 Northern Europe

Industry/Entity Type

Cosmetic/ Nail Gel Polish

Colors

Designer to choose only greyscale colors for use in the design.

Requirements
Must have
• See attched design instruction
Nice to have
• Moderne, Minimalist, Recognizable and Unique look
Should not have
• Too many elements, too busy design

```html
<!DOCTYPE html>
<html lang="en">
<head>
<meta charset="utf-8">
<title>LAKVIA Label Design</title>
<link href="https://fonts.googleapis.com/css2?family=Encode+Sans+Condensed:wght@400;600;700&family=Poppins:wght@300;400;500;600&display=swap" rel="stylesheet">
<style>
:root{
  --ink:#000;
  --paper:#fff;
  --bottle-hi:#4a4a4a;
  --frost:#f2f2f2;
  --blush:#e9bbaf;
  --velvet:#e8383b;
  --sorbet:#f08aa9;
  --remover:#5a5a5a;
}
*{box-sizing:border-box;margin:0;padding:0}
html,body{width:1200px;height:2171px;overflow:hidden;background:var(--paper)}
body{position:relative;font-family:"Poppins",sans-serif;color:var(--paper)}

.board-header{position:absolute;left:0;top:0;width:1200px;height:110px;background:var(--ink)}
.board-title{position:absolute;left:0;right:0;top:36px;text-align:center;font:700 28px/1 "Encode Sans Condensed",sans-serif}
.board-theme{position:absolute;right:10px;top:74px;font:400 17px/1 "Encode Sans Condensed",sans-serif}
.board-theme small{font-size:10px;margin-left:4px}

.board-footer{position:absolute;left:0;top:1930px;width:1200px;height:241px;background:var(--ink);text-align:center}
.footer-title{position:absolute;left:0;right:0;top:36px;font:700 30px/1 "Encode Sans Condensed",sans-serif}
.footer-note{position:absolute;left:0;right:0;top:82px;font:300 31px/1 "Poppins",sans-serif}

.bottle{position:absolute;width:84px;height:210px;border-radius:10px 10px 6px 6px;
  background:linear-gradient(90deg,#1a1a1a,var(--bottle-hi) 45%,#1a1a1a)}
.bottle--remover{width:80px;height:220px;border-radius:14px}

.label{position:absolute;width:524px;height:139px;background:var(--ink);overflow:hidden;color:var(--paper)}
.label--rim::before{content:"";position:absolute;left:0;top:0;right:0;height:4px;
  background:linear-gradient(90deg,#000,var(--tone) 30%,#000 50%,var(--tone) 80%,#000)}
.label-band{position:absolute;left:0;right:0;bottom:0;height:27px;
  background:linear-gradient(90deg,#000 0%,var(--tone) 14%,var(--tone) 36%,#000 50%,var(--tone) 64%,var(--tone) 88%,#000 100%)}
.label-front{position:absolute;left:0;top:0;width:248px;height:100%;text-align:center}
.brand{position:absolute;left:0;right:0;top:12px;font:300 31px/1 "Poppins",sans-serif;letter-spacing:.5px;color:var(--paper)}
.product{position:absolute;left:0;right:0;top:45px;font:400 11px/1 "Poppins",sans-serif;letter-spacing:.4px;color:var(--paper)}
.process{position:absolute;left:0;right:0;top:58px;font:300 5.5px/1 "Poppins",sans-serif}
.shade-no{position:absolute;left:0;right:0;top:67px;font:400 16px/1 "Poppins",sans-serif}
.volume{position:absolute;left:0;right:0;top:86px;font:300 7px/1 "Poppins",sans-serif}
.vegan{position:absolute;left:0;right:0;top:94px;height:17px;font:400 7px/1 "Poppins",sans-serif;letter-spacing:3.4px;display:flex;justify-content:center;align-items:center;gap:3px}
.vegan i{display:inline-block;width:17px;height:17px;border:1px solid #fff;border-radius:50%}
.shade-name{position:absolute;left:0;right:0;bottom:8px;font:500 10px/1 "Poppins",sans-serif;color:#111}
.shade-name--light{color:#fff}
.label-back{position:absolute;left:295px;top:16px;width:222px;font:300 4.3px/1.3 "Poppins",sans-serif}
.label-back b{font-weight:600}
.origin{text-align:center;font-size:5px;margin-top:1px;width:180px}
.marks{display:flex;justify-content:center;gap:3px;width:180px;margin-top:1px}
.mark{width:9px;height:9px;background:#fff}
.mark--round{border-radius:50%}
.maker{position:absolute;left:248px;right:0;bottom:5px;text-align:center;font:300 4px/1.3 "Poppins",sans-serif;color:#111}
.maker b{font-size:5.2px;font-weight:600;display:block}

.label--remover{width:440px;height:238px}
.remover-front{position:absolute;left:0;top:0;width:220px;height:100%;text-align:center}
.remover-front .brand{top:44px;font-size:32px}
.remover-band{position:absolute;left:0;right:0;top:102px;height:43px;background:linear-gradient(90deg,#000,var(--remover) 30%,var(--remover) 70%,#000)}
.remover-band span{position:absolute;left:0;right:0;top:7px;font:500 12px/1.2 "Poppins",sans-serif}
.remover-front .shade-no{top:160px;font-size:18px}
.remover-front .volume{top:214px;font-size:9px}
.remover-back{position:absolute;left:238px;top:50px;width:190px;font:300 4.3px/1.35 "Poppins",sans-serif}
.remover-back p{margin-bottom:4px}
.remover-maker{position:absolute;left:238px;width:190px;top:212px;text-align:center;font:300 4px/1.3 "Poppins",sans-serif}
.remover-maker b{font-size:5.2px;font-weight:600;display:block}
</style>
</head>
<body>

<header class="board-header">
  <h1 class="board-title">Label Design</h1>
  <p class="board-theme">Minimalist Vegan Design Theme<small>LKVA-LBD01</small></p>
</header>

<!-- Frost -->
<div class="bottle" style="left:287px;top:126px" role="img" aria-label="Product mockup: gel polish bottle wearing the Frost label"></div>
<section class="label" style="left:420px;top:158px;--tone:var(--frost)">
  <div class="label-band"></div>
  <div class="label-front">
    <div class="brand">lakvia</div><div class="product">COLOR COAT</div><div class="process">SOAK-OFF UV/LED</div>
    <div class="shade-no">08</div><div class="volume">12ml ⟡ 0.5oz</div>
    <div class="vegan">VEGAN<i></i>FORMULA</div><div class="shade-name">FROST</div>
  </div>
  <div class="label-back">
    <b>DIRECTIONS FOR USE (ENG):</b><br>Apply in thin layers and cure under one of our LED lamps.<br>
    <b>ANVENDELSE (DK):</b><br>Påføres i tynde lag og hærdes under en af vores lamper.<br>
    <b>CAUTION (ENG):</b><br>Keep out of reach of children. Stop use if irritation occurs.<br>
    <b>ADVARSEL (DK):</b><br>Opbevares utilgængeligt for børn. Stop ved irritation.<br>
    <b>INGREDIENTS:</b><br>Acrylates Copolymer, Urethane, Cellulose Acetate, Dimethicone, CI 77891
    <div class="origin">MADE IN EUROPE</div>
    <div class="marks"><span class="mark"></span><span class="mark"></span><span class="mark mark--round"></span><span class="mark"></span></div>
  </div>
  <div class="maker"><b>Nordhus Trading A/S</b>Elmegade 12, 2200 Copenhagen, Denmark</div>
</section>

<!-- Blush -->
<div class="bottle" style="left:287px;top:389px" role="img" aria-label="Product mockup: gel polish bottle wearing the Blush label"></div>
<section class="label label--rim" style="left:420px;top:424px;--tone:var(--blush)">
  <div class="label-band"></div>
  <div class="label-front">
    <div class="brand">lakvia</div><div class="product">COLOR COAT</div><div class="process">SOAK-OFF UV/LED</div>
    <div class="shade-no">14</div><div class="volume">12ml ⟡ 0.5oz</div>
    <div class="vegan">VEGAN<i></i>FORMULA</div><div class="shade-name">BLUSH</div>
  </div>
  <div class="label-back">
    <b>DIRECTIONS FOR USE (ENG):</b><br>Apply in thin layers and cure under one of our LED lamps.<br>
    <b>ANVENDELSE (DK):</b><br>Påføres i tynde lag og hærdes under en af vores lamper.<br>
    <b>CAUTION (ENG):</b><br>Keep out of reach of children. Stop use if irritation occurs.<br>
    <b>ADVARSEL (DK):</b><br>Opbevares utilgængeligt for børn. Stop ved irritation.<br>
    <b>INGREDIENTS:</b><br>Acrylates Copolymer, Urethane, Cellulose Acetate, Dimethicone, CI 77891
    <div class="origin">MADE IN EUROPE</div>
    <div class="marks"><span class="mark"></span><span class="mark"></span><span class="mark mark--round"></span><span class="mark"></span></div>
  </div>
  <div class="maker"><b>Nordhus Trading A/S</b>Elmegade 12, 2200 Copenhagen, Denmark</div>
</section>

<!-- Red Velvet -->
<div class="bottle" style="left:287px;top:654px" role="img" aria-label="Product mockup: gel polish bottle wearing the Red Velvet label"></div>
<section class="label" style="left:420px;top:685px;--tone:var(--velvet)">
  <div class="label-band"></div>
  <div class="label-front">
    <div class="brand">lakvia</div><div class="product">COLOR COAT</div><div class="process">SOAK-OFF UV/LED</div>
    <div class="shade-no">33</div><div class="volume">12ml ⟡ 0.5oz</div>
    <div class="vegan">VEGAN<i></i>FORMULA</div><div class="shade-name">RED VELVET</div>
  </div>
  <div class="label-back">
    <b>DIRECTIONS FOR USE (ENG):</b><br>Apply in thin layers and cure under one of our LED lamps.<br>
    <b>ANVENDELSE (DK):</b><br>Påføres i tynde lag og hærdes under en af vores lamper.<br>
    <b>CAUTION (ENG):</b><br>Keep out of reach of children. Stop use if irritation occurs.<br>
    <b>ADVARSEL (DK):</b><br>Opbevares utilgængeligt for børn. Stop ved irritation.<br>
    <b>INGREDIENTS:</b><br>Acrylates Copolymer, Urethane, Cellulose Acetate, Dimethicone, CI 77891
    <div class="origin">MADE IN GERMANY</div>
    <div class="marks"><span class="mark"></span><span class="mark"></span><span class="mark mark--round"></span><span class="mark"></span></div>
  </div>
  <div class="maker"><b>Nordhus Trading A/S</b>Elmegade 12, 2200 Copenhagen, Denmark</div>
</section>

<!-- Red Velvet, rim variant -->
<div class="bottle" style="left:287px;top:916px" role="img" aria-label="Product mockup: gel polish bottle wearing the Red Velvet label with red rim"></div>
<section class="label label--rim" style="left:420px;top:951px;--tone:var(--velvet)">
  <div class="label-band"></div>
  <div class="label-front">
    <div class="brand">lakvia</div><div class="product">COLOR COAT</div><div class="process">SOAK-OFF UV/LED</div>
    <div class="shade-no">33</div><div class="volume">12ml ⟡ 0.5oz</div>
    <div class="vegan">VEGAN<i></i>FORMULA</div><div class="shade-name">RED VELVET</div>
  </div>
  <div class="label-back">
    <b>DIRECTIONS FOR USE (ENG):</b><br>Apply in thin layers and cure under one of our LED lamps.<br>
    <b>ANVENDELSE (DK):</b><br>Påføres i tynde lag og hærdes under en af vores lamper.<br>
    <b>CAUTION (ENG):</b><br>Keep out of reach of children. Stop use if irritation occurs.<br>
    <b>ADVARSEL (DK):</b><br>Opbevares utilgængeligt for børn. Stop ved irritation.<br>
    <b>INGREDIENTS:</b><br>Acrylates Copolymer, Urethane, Cellulose Acetate, Dimethicone, CI 77891
    <div class="origin">MADE IN GERMANY</div>
    <div class="marks"><span class="mark"></span><span class="mark"></span><span class="mark mark--round"></span><span class="mark"></span></div>
  </div>
  <div class="maker"><b>Nordhus Trading A/S</b>Elmegade 12, 2200 Copenhagen, Denmark</div>
</section>

<!-- Pink Sorbet -->
<div class="bottle" style="left:282px;top:1157px" role="img" aria-label="Product mockup: gel polish bottle wearing the Pink Sorbet label"></div>
<section class="label" style="left:415px;top:1208px;--tone:var(--sorbet)">
  <div class="label-band"></div>
  <div class="label-front">
    <div class="brand">lakvia</div><div class="product">COLOR COAT</div><div class="process">SOAK-OFF UV/LED</div>
    <div class="shade-no">57</div><div class="volume">12ml ⟡ 0.5oz</div>
    <div class="vegan">VEGAN<i></i>FORMULA</div><div class="shade-name">PINK SORBET</div>
  </div>
  <div class="label-back">
    <b>DIRECTIONS FOR USE (ENG):</b><br>Apply in thin layers and cure under one of our LED lamps.<br>
    <b>ANVENDELSE (DK):</b><br>Påføres i tynde lag og hærdes under en af vores lamper.<br>
    <b>CAUTION (ENG):</b><br>Keep out of reach of children. Stop use if irritation occurs.<br>
    <b>ADVARSEL (DK):</b><br>Opbevares utilgængeligt for børn. Stop ved irritation.<br>
    <b>INGREDIENTS:</b><br>Acrylates Copolymer, Urethane, Cellulose Acetate, Dimethicone, CI 77891
    <div class="origin">MADE IN GERMANY</div>
    <div class="marks"><span class="mark"></span><span class="mark"></span><span class="mark mark--round"></span><span class="mark"></span></div>
  </div>
  <div class="maker"><b>Nordhus Trading A/S</b>Elmegade 12, 2200 Copenhagen, Denmark</div>
</section>

<!-- Pink Sorbet, rim variant -->
<div class="bottle" style="left:282px;top:1419px" role="img" aria-label="Product mockup: gel polish bottle wearing the Pink Sorbet label with pink rim"></div>
<section class="label label--rim" style="left:415px;top:1475px;--tone:var(--sorbet)">
  <div class="label-band"></div>
  <div class="label-front">
    <div class="brand">lakvia</div><div class="product">COLOR COAT</div><div class="process">SOAK-OFF UV/LED</div>
    <div class="shade-no">57</div><div class="volume">12ml ⟡ 0.5oz</div>
    <div class="vegan">VEGAN<i></i>FORMULA</div><div class="shade-name">PINK SORBET</div>
  </div>
  <div class="label-back">
    <b>DIRECTIONS FOR USE (ENG):</b><br>Apply in thin layers and cure under one of our LED lamps.<br>
    <b>ANVENDELSE (DK):</b><br>Påføres i tynde lag og hærdes under en af vores lamper.<br>
    <b>CAUTION (ENG):</b><br>Keep out of reach of children. Stop use if irritation occurs.<br>
    <b>ADVARSEL (DK):</b><br>Opbevares utilgængeligt for børn. Stop ved irritation.<br>
    <b>INGREDIENTS:</b><br>Acrylates Copolymer, Urethane, Cellulose Acetate, Dimethicone, CI 77891
    <div class="origin">MADE IN GERMANY</div>
    <div class="marks"><span class="mark"></span><span class="mark"></span><span class="mark mark--round"></span><span class="mark"></span></div>
  </div>
  <div class="maker"><b>Nordhus Trading A/S</b>Elmegade 12, 2200 Copenhagen, Denmark</div>
</section>

<!-- Remover -->
<div class="bottle bottle--remover" style="left:343px;top:1680px" role="img" aria-label="Product mockup: gel polish remover bottle with its label"></div>
<section class="label label--remover" style="left:468px;top:1667px">
  <div class="remover-front">
    <div class="brand">lakvia</div>
    <div class="remover-band"><span>GEL POLISH<br>REMOVER</span></div>
    <div class="shade-no">90</div>
    <div class="volume">120ml ⟡ 4 fl.oz</div>
  </div>
  <div class="remover-back">
    <p><b>DIRECTIONS FOR USE (ENG):</b><br>Soak a lint free wipe with the remover, place it on the nail and wrap in foil for 15 minutes. Remove the foil and gently push off the softened gel. Repeat if needed. Moisturise your nails after treatment.</p>
    <p><b>ANVENDELSESGUIDE (DK):</b><br>Fugt en fnugfri serviet med fjerneren, læg den på neglen og pak ind i folie i 15 minutter. Fjern folien og skub gelen forsigtigt af. Gentag ved behov. Fugt neglene efter behandling.</p>
    <p><b>CAUTION (ENG):</b><br>Keep out of reach of children. Discontinue use if sensitivity occurs.</p>
    <p><b>ADVARSEL (DK):</b><br>Opbevares utilgængeligt for børn. Stop ved irritation.</p>
    <p><b>INGREDIENTS:</b><br>Ethyl acetate, n-butyl acetate, Acetone, Isopropyl alcohol, glycerin</p>
    <div class="marks" style="width:190px"><span class="mark mark--round"></span></div>
  </div>
  <div class="remover-maker"><b>Nordhus Trading A/S</b>Elmegade 12, 2200 Copenhagen, Denmark</div>
</section>

<footer class="board-footer">
  <h2 class="footer-title">“LAKVIA” Label</h2>
  <p class="footer-note">Illustration for presentation purpose only</p>
</footer>

</body>
</html>
```